Innovation Presentation Template

I need a unique template design for a presentation on Innovation used exclusively inside of our company. I'd prefer to work in Apple Keynote but can take a .ppt and convert it. The template should appeal to a broad audience of diverse job descriptions. This is a one-time presentation that will last between 30 and 45 minutes. The design should provide a strong visual appeal with multiple chart layouts to support highlighted test points (no bullets, I hate bullets), graphics, line art, and video/photos. My presentations are sparse, never more that 2 concepts per chart (usually one). Our company is a high tech manufacturer selling products in many markets ranging from Government to consumer. The final design should include style a style guide including suggested fonts, colors, graph formats, suggested word art, etc.

Target Market(s)

The audience is internal employees only. Strong corporate branding is not required in this presentation.

Industry/Entity Type

Government

Colors
3277b5
faa54b

Requirements
Must have
• Strong visual appeal helping to support the communication of simple concepts (that have been broken down from complex subject matter).

Multiple chart template forms to support different forms of communication including text points, data charts, graphics, photos, and videos.

Visuals will be memorable, but not overpower the content. Visuals will help convey the content.

Well conceived and coordinated color pallets. Fonts guides (that I can access).

You can visit our company web site at www.vantrel-example.com to see logo and corporate look/feel. It would be good to build logo into a few of the chart templates, but not all.
Nice to have
• Keynote (please). I can live with .ppt if I have to.

Many charts will make a point with simple single sentences. Find a way to make the sentences graphically interesting by varying font and/or color of specific words to help drive points.

Note that colors that I've identified below are based upon the blue used in our logo and the orange that complements it. I'm not married to these but use them as guidelines.
Should not have
• Noise. Corporate nauseia.

```html
<!DOCTYPE html>
<html lang="en">
<head>
<meta charset="utf-8">
<title>Innovation Presentation Template – Vantrel</title>
<link href="https://fonts.googleapis.com/css2?family=Open+Sans:wght@300;400;600;700;800&display=swap" rel="stylesheet">
<style>
:root{
  --page:#d9d9d9;
  --white:#ffffff;
  --blue:#3277b5;
  --blue-deep:#2c63a8;
  --blue-dark:#245a99;
  --blue-mid:#3a86c6;
  --blue-light:#4fa9e0;
  --blue-pale:#8ccaef;
  --orange:#faa54b;
  --orange-strong:#f7923a;
  --text:#4a4a4a;
  --grid:#e3e3e3;
}
*{box-sizing:border-box;margin:0;padding:0}
html,body{width:900px;height:1200px;overflow:hidden}
body{background:var(--page);position:relative;font-family:"Open Sans",Arial,sans-serif;color:var(--text)}
.slide{position:absolute;width:382px;height:214px;background:var(--white);overflow:hidden}
.slide--blue{background:var(--blue-deep)}
.slide--orange{background:var(--orange-strong)}
.col-left{left:49px}.col-right{left:450px}
.row-1{top:68px}.row-2{top:322px}.row-3{top:575px}.row-4{top:829px}

.brand{position:absolute;font-weight:800;letter-spacing:.5px;color:var(--blue);display:flex;align-items:center;gap:4px}
.brand::before{content:"";width:.7em;height:.7em;background:currentColor}
.brand--large{right:24px;top:138px;font-size:20px}
.brand--white{color:var(--white);right:16px;top:173px;font-size:16px}
.brand--small{right:14px;bottom:9px;font-size:9px}

.pattern{position:absolute;left:0;bottom:0;clip-path:polygon(0 100%,0 70%,30% 45%,55% 20%,70% 0,88% 30%,100% 45%,100% 75%,60% 90%,30% 100%)}
.pattern--cover{width:290px;height:110px;background:linear-gradient(90deg,var(--blue) 0%,var(--orange) 45%,var(--blue) 75%,var(--orange) 100%)}
.pattern--light{width:240px;height:100px;background:linear-gradient(90deg,rgba(255,255,255,.95),rgba(255,255,255,.75))}

.cover-title{position:absolute;left:0;right:0;top:38px;text-align:center;color:var(--blue);font-weight:400;font-size:15px}
.cover-sub{position:absolute;left:0;right:0;top:62px;text-align:center;color:var(--orange);font-size:8px}
.thanks-title{position:absolute;left:0;right:0;top:50px;text-align:center;color:var(--blue);font-size:15px}

.section-title{position:absolute;left:14px;top:52px;color:var(--white);font-size:14px;font-weight:400}
.section-sub{position:absolute;left:14px;top:72px;color:var(--white);font-size:10px;font-weight:300;opacity:.9}
.slide--orange .section-sub{opacity:.8}

.slide-title{position:absolute;left:24px;top:22px;color:var(--blue);font-size:15px;font-weight:400}
.overview-title{left:18px;top:17px;font-size:17px}
.overview-sub{position:absolute;left:18px;top:38px;color:var(--blue);font-size:7.2px}
.overview-body{position:absolute;left:18px;right:16px;top:55px;font-size:4.6px;line-height:1.3;color:#555}
.overview-body p{margin-bottom:4px}

/* historical chart */
.hist-chart{position:absolute;left:40px;top:60px;width:198px;height:124px}
.axis-y{position:absolute;left:0;top:0;bottom:10px;width:22px;display:flex;flex-direction:column;justify-content:space-between;font-size:4px;text-align:right}
.plot{position:absolute;left:26px;right:0;top:3px;bottom:12px;border-bottom:1px solid #bbb;
  background:repeating-linear-gradient(to top,var(--grid) 0 1px,transparent 1px 13.6px);
  display:flex;align-items:flex-end;justify-content:space-around;padding:0 3px}
.stack{width:11px;display:flex;flex-direction:column-reverse}
.seg-gov{background:var(--blue-dark)}.seg-us{background:var(--blue-mid)}.seg-eu{background:var(--blue-light)}.seg-row{background:var(--blue-pale)}
.axis-x{position:absolute;left:26px;right:0;bottom:3px;display:flex;justify-content:space-around;font-size:4px;padding:0 1px}
.axis-note{position:absolute;left:4px;top:-4px;font-size:3.4px}

.growth-table{position:absolute;left:236px;top:67px;border-collapse:separate;border-spacing:1px;font-size:5px}
.growth-table th{background:var(--blue);color:var(--white);font-weight:400;height:12px;padding:0 4px;font-size:5.5px}
.growth-table td{height:20px;text-align:center;width:38px}
.growth-table .label{background:none;text-align:left;width:auto;color:#333;font-weight:600;padding-right:3px}
.growth-table .c-ten{background:var(--blue-light);color:var(--white)}
.growth-table .c-five{background:var(--orange);color:var(--white)}
.growth-table .sub th{background:none;height:auto}
.growth-table .h-ten{background:var(--blue-light)!important;height:14px!important;font-size:4px!important}
.growth-table .h-five{background:var(--orange)!important;height:14px!important;font-size:4px!important}

/* market trends */
.market-tabs{position:absolute;left:24px;top:52px;width:332px;display:flex;gap:6px}
.market-tab{flex:1;background:var(--blue);color:var(--white);font-size:4.6px;text-align:center;height:9px;line-height:9px}
.market-note{position:absolute;left:24px;top:64px;font-size:3.6px}
.market-axis{position:absolute;left:22px;top:70px;height:114px;display:flex;flex-direction:column;justify-content:space-between;font-size:3.8px}
.market-plot{position:absolute;left:34px;right:26px;top:72px;height:112px;border-bottom:1px solid #bbb;
  background:repeating-linear-gradient(to top,var(--grid) 0 1px,transparent 1px 22.4px);display:flex;gap:8px}
.market-group{flex:1;position:relative;display:flex;align-items:flex-end;justify-content:space-between}
.mbar{width:11px;background:var(--orange-strong)}
.badge{position:absolute;left:50%;top:50px;width:38px;margin-left:-19px}
.badge svg{display:block}
.badge-text{position:absolute;left:0;right:0;top:16px;text-align:center;color:var(--white);font-size:8px;line-height:1}
.badge-text small{display:block;font-size:3.6px;margin-top:1px}
.market-years{position:absolute;left:34px;right:26px;top:187px;display:flex;gap:8px;font-size:3.2px}
.market-years span{flex:1;display:flex;justify-content:space-between}
</style>
</head>
<body>

<!-- Cover -->
<section class="slide col-left row-1">
  <h1 class="cover-title">Presentation Template (Cover)</h1>
  <p class="cover-sub">Sub Heading</p>
  <div class="pattern pattern--cover" role="img" aria-label="Rising band of blue and orange diamond tiles"></div>
  <div class="brand brand--large">VANTREL</div>
</section>

<!-- Section blue -->
<section class="slide slide--blue col-right row-1">
  <h2 class="section-title">SECTION HEADING</h2>
  <p class="section-sub">Sub heading</p>
  <div class="pattern pattern--light" role="img" aria-label="Rising band of white diamond tiles"></div>
  <div class="brand brand--white">VANTREL</div>
</section>

<!-- Section orange -->
<section class="slide slide--orange col-left row-2">
  <h2 class="section-title">SECTION HEADING</h2>
  <p class="section-sub">Sub heading</p>
  <div class="pattern pattern--light" role="img" aria-label="Rising band of white diamond tiles"></div>
  <div class="brand brand--white">VANTREL</div>
</section>

<!-- Company overview -->
<section class="slide col-right row-2">
  <h2 class="slide-title overview-title">Company Overview</h2>
  <p class="overview-sub">The World Leader in the Design, Manufacture and Marketing of Thermal Imaging Infrared Cameras</p>
  <div class="overview-body">
    <p>Vantrel was founded in 1978, originally providing infrared imaging systems installed on vehicles for use in conducting energy audits. We later expanded our focus to other applications and markets for thermal imaging technology, such as stabilized camera systems for law enforcement aircraft, radiometric devices for monitoring industrial systems, and imaging systems for ground-based security and search and rescue. We have since grown substantially through rising demand and a series of acquisitions, and today we are a leader in the design and marketing of sensor systems for commercial, industrial and government markets worldwide.</p>
    <p>Our Commercial Systems business designs and manufactures products for a wide variety of emerging industrial and commercial markets where the primary requirement is to see in total darkness or to detect and measure small temperature differences. These products serve building inspection, electrical maintenance, research and development, automotive night vision, firefighting and process control. We sell through a broad distribution network, which allows us to reduce costs and open new markets.</p>
    <p>Our Government Systems business is focused on markets where high performance situational awareness tools are required. We design, manufacture and market thermal imaging and radar surveillance systems and chemical and explosive detection products. Customers use them for border and maritime patrol, force protection, search and rescue and threat detection, and we continue to grow our program business in the United States and abroad.</p>
  </div>
  <div class="brand brand--small">VANTREL</div>
</section>

<!-- Historical performance -->
<section class="slide col-left row-3">
  <h2 class="slide-title">Historical Performance</h2>
  <div class="hist-chart">
    <span class="axis-note">Revenue in millions</span>
    <div class="axis-y"><span>$1,600</span><span>$1,400</span><span>$1,200</span><span>$1,000</span><span>$800</span><span>$600</span><span>$400</span><span>$200</span><span>$0</span></div>
    <div class="plot">
      <div class="stack"><i class="seg-gov" style="height:8px"></i><i class="seg-us" style="height:5px"></i><i class="seg-eu" style="height:4px"></i><i class="seg-row" style="height:3px"></i></div>
      <div class="stack"><i class="seg-gov" style="height:12px"></i><i class="seg-us" style="height:8px"></i><i class="seg-eu" style="height:6px"></i><i class="seg-row" style="height:5px"></i></div>
      <div class="stack"><i class="seg-gov" style="height:13px"></i><i class="seg-us" style="height:8px"></i><i class="seg-eu" style="height:7px"></i><i class="seg-row" style="height:5px"></i></div>
      <div class="stack"><i class="seg-gov" style="height:14px"></i><i class="seg-us" style="height:9px"></i><i class="seg-eu" style="height:7px"></i><i class="seg-row" style="height:6px"></i></div>
      <div class="stack"><i class="seg-gov" style="height:20px"></i><i class="seg-us" style="height:13px"></i><i class="seg-eu" style="height:10px"></i><i class="seg-row" style="height:8px"></i></div>
      <div class="stack"><i class="seg-gov" style="height:28px"></i><i class="seg-us" style="height:18px"></i><i class="seg-eu" style="height:14px"></i><i class="seg-row" style="height:10px"></i></div>
      <div class="stack"><i class="seg-gov" style="height:30px"></i><i class="seg-us" style="height:19px"></i><i class="seg-eu" style="height:15px"></i><i class="seg-row" style="height:11px"></i></div>
      <div class="stack"><i class="seg-gov" style="height:36px"></i><i class="seg-us" style="height:22px"></i><i class="seg-eu" style="height:18px"></i><i class="seg-row" style="height:14px"></i></div>
      <div class="stack"><i class="seg-gov" style="height:40px"></i><i class="seg-us" style="height:25px"></i><i class="seg-eu" style="height:20px"></i><i class="seg-row" style="height:15px"></i></div>
      <div class="stack"><i class="seg-gov" style="height:36px"></i><i class="seg-us" style="height:23px"></i><i class="seg-eu" style="height:18px"></i><i class="seg-row" style="height:14px"></i></div>
      <div class="stack"><i class="seg-gov" style="height:39px"></i><i class="seg-us" style="height:25px"></i><i class="seg-eu" style="height:20px"></i><i class="seg-row" style="height:14px"></i></div>
    </div>
    <div class="axis-x"><span>2003</span><span>2004</span><span>2005</span><span>2006</span><span>2007</span><span>2008</span><span>2009</span><span>2010</span><span>2011</span><span>2012</span><span>2013</span></div>
  </div>
  <table class="growth-table">
    <tr><th></th><th colspan="2">Revenue Growth</th></tr>
    <tr class="sub"><th></th><th class="h-ten">10yr CAGR</th><th class="h-five">5yr</th></tr>
    <tr><td class="label">ROW</td><td class="c-ten">20%</td><td class="c-five">4%</td></tr>
    <tr><td class="label">Europe</td><td class="c-ten">15%</td><td class="c-five">13%</td></tr>
    <tr><td class="label">U.S.</td><td class="c-ten">15%</td><td class="c-five">-16%</td></tr>
    <tr><td class="label">U.S. Gov't</td><td class="c-ten">16%</td><td class="c-five">3%</td></tr>
  </table>
  <div class="brand brand--small">VANTREL</div>
</section>

<!-- Long term market trends -->
<section class="slide col-right row-3">
  <h2 class="slide-title">Long Term Market Trends</h2>
  <div class="market-tabs">
    <span class="market-tab">U.S. (Ex U.S. Gov't)</span>
    <span class="market-tab">U.S. Government</span>
    <span class="market-tab">Europe</span>
    <span class="market-tab">Rest of World</span>
  </div>
  <span class="market-note">Revenue in millions</span>
  <div class="market-axis"><span>$500</span><span>$400</span><span>$300</span><span>$200</span><span>$100</span><span>$0</span></div>
  <div class="market-plot">
    <div class="market-group">
      <i class="mbar" style="height:40px"></i><i class="mbar" style="height:60px"></i><i class="mbar" style="height:81px"></i><i class="mbar" style="height:76px"></i><i class="mbar" style="height:92px"></i>
      <div class="badge"><svg width="38" height="36" viewBox="0 0 38 36"><polygon points="19,0 38,14 38,36 0,36 0,14" fill="#3277b5"/></svg><div class="badge-text">23%<small>5yr CAGR</small></div></div>
    </div>
    <div class="market-group">
      <i class="mbar" style="height:110px"></i><i class="mbar" style="height:105px"></i><i class="mbar" style="height:101px"></i><i class="mbar" style="height:85px"></i><i class="mbar" style="height:81px"></i>
      <div class="badge" style="top:20px"><svg width="38" height="36" viewBox="0 0 38 36"><polygon points="0,0 38,0 38,22 19,36 0,22" fill="#3277b5"/></svg><div class="badge-text" style="top:6px">-8%<small>5yr CAGR</small></div></div>
    </div>
    <div class="market-group">
      <i class="mbar" style="height:56px"></i><i class="mbar" style="height:72px"></i><i class="mbar" style="height:85px"></i><i class="mbar" style="height:78px"></i><i class="mbar" style="height:83px"></i>
      <div class="badge"><svg width="38" height="36" viewBox="0 0 38 36"><polygon points="19,0 38,14 38,36 0,36 0,14" fill="#3277b5"/></svg><div class="badge-text">11%<small>5yr CAGR</small></div></div>
    </div>
    <div class="market-group">
      <i class="mbar" style="height:56px"></i><i class="mbar" style="height:76px"></i><i class="mbar" style="height:81px"></i><i class="mbar" style="height:80px"></i><i class="mbar" style="height:83px"></i>
      <div class="badge"><svg width="38" height="36" viewBox="0 0 38 36"><polygon points="19,0 38,14 38,36 0,36 0,14" fill="#3277b5"/></svg><div class="badge-text">12%<small>5yr CAGR</small></div></div>
    </div>
  </div>
  <div class="market-years">
    <span><b>2008</b><b>2010</b><b>2011</b><b>2012</b><b>2013</b></span>
    <span><b>2008</b><b>2010</b><b>2011</b><b>2012</b><b>2013</b></span>
    <span><b>2008</b><b>2010</b><b>2011</b><b>2012</b><b>2013</b></span>
    <span><b>2008</b><b>2010</b><b>2011</b><b>2012</b><b>2013</b></span>
  </div>
  <div class="brand brand--small">VANTREL</div>
</section>

<!-- Closing -->
<section class="slide col-left row-4">
  <h2 class="thanks-title">Thank you</h2>
  <div class="pattern pattern--cover" role="img" aria-label="Rising band of blue and orange diamond tiles"></div>
  <div class="brand brand--large">VANTREL</div>
</section>

</body>
</html>
```